LunaForm Informational Flyer Design

Hello, we are a team of two who opened an all women's gym located in Seattle, WA. We've been in business for four and a half years renting from various other facilities such as crossfit, a banquet hall, and outside at local parks, and opened our own facility in January 2016.
Check www.lunaformstudio-example.com for more info about our gym, our team, and what we offer to our clients.
We are looking for a strong, clean, but feminine double-sided leaflet or something a little larger than the average postcard to pass out to local businesses, schools and other charitable auctions, and neighboring apartment buildings that are currently under construction. DL size
We have more images should you need them for the design, some more abstract of just equipment; included a few here along with our logo.
Please let me know if you need more info or more pics.
Thanks in advance!

Hello, I have updated the brief with more specifics. Please take a look and resubmit with thanks. Added Thursday, February 16, 2017

Target Market(s)

Women ages 18-70

Industry/Entity Type

Fitness

Font styles to use
Other font styles liked:
• Futura (SEE NOTES)

Colors
e34197
000000

Requirements
Must have
• DL Size
• Front should be clean and simple and include:
• • LOGO
• • RESULTS-DRIVEN WOMEN’S FITNESS
• • FREE INTRODUCTORY WEEK
• • pictures of LUNAPULSE, LUNAPOISE, & LUNAFLOW with names overlaid on pictures (see home page of website)
• ◦ *CHILDCARE INCLUDED (underneath program pictures, but not too big)
• BACK side:
• • LunaForm is not just a women's gym. We are a community of women grinding and growing into the very best versions of ourselves.  LunaForm’s mission is simple -- to get you strong, balanced, and flexible for life both in and out of the gym.
• • PROGRAMS:   (Optional to include pictures of each program)
• LUNAPULSE underneath should list ASCEND & LUNAFIRST
• LUNAPOISE
• LUNAFLOW underneath should list LUNA STRONG STREAM & RESTORATIVE YOGA
• • PRICING (includes childcare)
• ANNUAL $1675
• MONTHLY $159
• 10 CLASS PASS $199
• DROP-IN $25
• *See website for special discounts*
• • Phone
• • Email
• • Address
• • Website
• • COUPON CODE section with some space underneath to handwrite in a coupon code. 
Nice to have
• If it works with the design and doesn't make it too cluttered, instead of FREE INTRODUCTORY WEEK on front side, can say CLAIM YOUR FREE INTRO WEEK HERE (or some other wording) and include a QR code that goes directly to our scheduling site: https://lunaform.bookdeskapp-example.com/welcome
• Can use the fonts in the logo or designer preference on what will work best with design.

```html
<!DOCTYPE html>
<html lang="en">
<head>
<meta charset="utf-8">
<title>LunaForm DL Flyer</title>
<link rel="stylesheet" href="https://fonts.googleapis.com/css2?family=Jost:wght@400;500;600;700;800&family=Oswald:wght@500&display=swap">
<style>
  :root {
    --pink: #d41c84;
    --pink-soft: #e34197;
    --plum: #5e0f3c;
    --black: #000000;
    --white: #ffffff;
    --stage: #2c2c2c;
    --split: 210px;
  }
  * { box-sizing: border-box; margin: 0; padding: 0; }
  html, body { width: 1200px; height: 1200px; overflow: hidden; background: var(--stage); }
  body { position: relative; font-family: "Jost", sans-serif; color: var(--white); }

  .card {
    position: absolute; top: 122px; width: 446px; height: 946px; overflow: hidden;
    background: linear-gradient(to right, var(--pink) 0 var(--split), var(--black) var(--split) 100%);
    box-shadow: 0 10px 30px rgba(0,0,0,.5);
  }
  .card--front { left: 132px; }
  .card--back { left: 643px; }

  .backdrop {
    position: absolute; left: 0; right: 0; top: 450px; bottom: 0;
    background:
      radial-gradient(ellipse 120px 160px at 150px 120px, rgba(255,255,255,.16), transparent 70%),
      radial-gradient(ellipse 160px 220px at 330px 260px, rgba(212,28,132,.18), transparent 70%),
      linear-gradient(to bottom, rgba(0,0,0,.05), rgba(0,0,0,.2));
  }
  .card--back .backdrop { top: 440px; }

  .brand { position: absolute; top: 56px; left: 0; width: 100%; text-align: center; }
  .brand__name { font-weight: 600; font-size: 52px; line-height: 1; letter-spacing: 4px; }
  .brand__tagline { margin-top: 8px; font-weight: 400; font-size: 25px; letter-spacing: 5px; line-height: 1; }

  .headline { position: absolute; top: 176px; left: 34px; font-weight: 700; font-size: 19px; letter-spacing: .2px; white-space: nowrap; }
  .headline__dark { color: var(--black); }

  .offer { position: absolute; font-weight: 800; font-size: 37px; line-height: 1; white-space: nowrap; }
  .offer--free { top: 216px; left: 122px; }
  .offer--intro { top: 248px; left: 72px; height: 42px; padding: 3px 0 0 18px; width: 320px; background: var(--black); border-radius: 21px; }
  .offer--week { top: 293px; left: 98px; }

  .tile { position: absolute; border-radius: 18px; background: var(--plum); }
  .tile__photo { position: absolute; inset: 8px; border-radius: 12px; display: flex; align-items: center; justify-content: center; }
  .tile__label { font-family: "Oswald", sans-serif; font-weight: 500; color: var(--white); text-shadow: 0 1px 3px rgba(0,0,0,.6); letter-spacing: -.5px; }
  .tile--flow { left: 262px; top: 366px; width: 123px; height: 113px; }
  .tile--flow .tile__photo { background: linear-gradient(160deg, #cfc6bd, #8a6f66 55%, #c2566f); }
  .tile--flow .tile__label { font-size: 19px; }
  .tile--poise { left: 110px; top: 472px; width: 163px; height: 154px; background: var(--pink); }
  .tile--poise .tile__photo { background: linear-gradient(150deg, #ece7e2, #bdb3ac 50%, #e9e2dc); }
  .tile--poise .tile__label { font-size: 28px; }
  .tile--pulse { left: 250px; top: 614px; width: 220px; height: 316px; border-radius: 26px; }
  .tile--pulse .tile__photo { inset: 20px 24px 18px 20px; border-radius: 18px; background: linear-gradient(170deg, #d9dadb, #8a8a8c 45%, #2f2f33); justify-content: flex-end; padding-right: 8px; }
  .tile--pulse .tile__label { font-size: 36px; }

  .childcare { position: absolute; left: 0; top: 828px; width: var(--split); height: 67px; background: var(--black); text-align: right; padding: 5px 2px 0 0; font-weight: 700; font-size: 27px; line-height: 29px; }
  .childcare__mark { color: var(--pink); }

  .about { position: absolute; top: 161px; left: 53px; width: 324px; font-size: 9.6px; line-height: 15px; text-align: justify; text-transform: uppercase; }

  .section-title { position: absolute; font-weight: 700; font-size: 25px; line-height: 1; border-bottom: 1.5px solid var(--white); padding-bottom: 2px; }
  .section-title--programs { top: 298px; left: 43px; width: 286px; }
  .section-title--pricing { top: 520px; left: 83px; width: 300px; }

  .programs { position: absolute; top: 330px; left: 191px; list-style: none; }
  .program { position: relative; padding-left: 23px; margin-bottom: 8px; }
  .program::before { content: ""; position: absolute; left: 0; top: 12px; width: 12px; height: 12px; border-radius: 3px; background: var(--white); }
  .program__name { color: var(--pink-soft); font-size: 27px; line-height: 30px; letter-spacing: 1.5px; }
  .program__detail { font-size: 13px; line-height: 16px; letter-spacing: 1.2px; }

  .pricing { position: absolute; top: 560px; left: 215px; list-style: none; font-size: 21.5px; line-height: 34.5px; white-space: nowrap; }
  .pricing b { font-weight: 700; }

  .website { position: absolute; left: var(--split); right: 0; top: 738px; height: 37px; background: var(--pink); font-weight: 700; font-style: italic; font-size: 12.5px; padding: 10px 0 0 5px; letter-spacing: 0; white-space: nowrap; }

  .coupon { position: absolute; left: 0; top: 784px; width: 179px; height: 79px; background: var(--white); border-radius: 0 14px 14px 0; color: var(--black); font-weight: 700; font-size: 17px; padding: 10px 0 0 22px; }

  .contact { position: absolute; top: 794px; left: 217px; font-style: normal; font-size: 14.5px; line-height: 17px; letter-spacing: .6px; white-space: nowrap; }
  .contact__phone { font-weight: 700; margin-bottom: 7px; letter-spacing: 1px; }
  .contact__email { color: var(--pink-soft); font-size: 10px; letter-spacing: .3px; margin-top: 10px; }
</style>
</head>
<body>

<section class="card card--front" aria-label="Flyer front">
  <div class="backdrop" role="img" aria-label="Faded photo of women training, blended into the background"></div>

  <header class="brand">
    <div class="brand__name">LUNAFORM</div>
    <div class="brand__tagline">YOU WILL ASCEND</div>
  </header>

  <p class="headline"><span class="headline__dark">RESULTS-DRIVEN</span> WOMEN’S FITNESS</p>

  <div class="offer offer--free">FREE</div>
  <div class="offer offer--intro">INTRODUCTORY</div>
  <div class="offer offer--week">WEEK</div>

  <div class="tile tile--flow">
    <div class="tile__photo" role="img" aria-label="Photo of a yoga class in downward dog"><span class="tile__label">LUNAFLOW</span></div>
  </div>
  <div class="tile tile--poise">
    <div class="tile__photo" role="img" aria-label="Photo of a barre class stretching"><span class="tile__label">LUNAPOISE</span></div>
  </div>
  <div class="tile tile--pulse">
    <div class="tile__photo" role="img" aria-label="Photo of women lifting kettlebells in a row"><span class="tile__label">LUNAPULSE</span></div>
  </div>

  <div class="childcare"><span class="childcare__mark">*CHILDCARE</span><br>INCLUDED</div>
</section>

<section class="card card--back" aria-label="Flyer back">
  <div class="backdrop" role="img" aria-label="Faded photo of a woman training with a kettlebell"></div>

  <header class="brand">
    <div class="brand__name">LUNAFORM</div>
    <div class="brand__tagline">YOU WILL ASCEND</div>
  </header>

  <p class="about">LunaForm is not just a women’s gym. We are a community of women who seek beauty in strength; who see each new day as a chance to better ourselves; who find confidence in pushing through the challenges thrown in our paths. At LunaForm, your membership includes all three program choices with childcare included because our mission is simple -- to get you strong, balanced, and flexible for life both in and out of the gym.</p>

  <h2 class="section-title section-title--programs">PROGRAMS:</h2>
  <ul class="programs">
    <li class="program"><div class="program__name">LUNAPULSE</div><div class="program__detail">ASCEND &amp; LUNAFIRST</div></li>
    <li class="program"><div class="program__name">LUNAPOISE</div></li>
    <li class="program"><div class="program__name">LUNAFLOW</div><div class="program__detail">LUNA STRONG STREAM &amp;<br>RESTORATIVE YOGA</div></li>
  </ul>

  <h2 class="section-title section-title--pricing">PRICING:</h2>
  <ul class="pricing">
    <li>ANNUAL <b>$1675</b></li>
    <li>MONTHLY <b>$159</b></li>
    <li>10 CLASS PASS <b>$199</b></li>
    <li>DROP-IN <b>$25</b></li>
  </ul>

  <div class="website">LUNAFORMSTUDIO-EXAMPLE.COM</div>

  <div class="coupon">COUPON CODE</div>

  <address class="contact">
    <div class="contact__phone">206.555.0147</div>
    <div>1520 HARBOR CREST AVE SW</div>
    <div>SEATTLE, WA 98126</div>
    <div class="contact__email">ASCEND@LUNAFORMSTUDIO-EXAMPLE.COM</div>
  </address>
</section>

</body>
</html>
```